Bright Harbor Family Law Firm Website Renovation

We need a website redesign in SquareSpace that is more modern, user friendly, on brand, less cluttered, easier to navigate, conveys clearly what our services are, and has clear, visible calls to action.

We would like to hire and work with the winning designer to complete the remaining pages of the site.
Updates

Gathering more feedback

Target Market(s)

Couples looking for divorce representation or mediation who have a conscious, progressive mindset. They are self-aware and personal development plays an important role in their lives. They want an amicable interaction and aspire to have a healthy relationship after divorce.

Age range: 30-60
Income 100K+ household

Industry/Entity Type

Family Law

Font styles to use
Sans Serif

Colors
85acd3
33a6d7
50c0af
a0cd3a

Requirements
Must have
• Please see attached doc for full creative brief details.

"Changing the way people divorce" on top of site.
Images that show happy clients and that represent males and females. Diversity inclusion is also be important.
We are looking for warm, welcoming design and imagery.
Should not have
• Not heavily attorney focused.
Please see attached brief for full description.

```html
<!DOCTYPE html>
<html lang="en">
<head>
<meta charset="utf-8">
<title>Bright Harbor Family Law</title>
<link href="https://fonts.googleapis.com/css2?family=Libre+Baskerville:wght@400;700&family=Open+Sans:wght@300;400;600&display=swap" rel="stylesheet">
<style>
:root{
  --blue:#33a6d7;
  --teal:#50c0af;
  --lime:#a0cd3a;
  --soft-blue:#85acd3;
  --ink:#1d1d1d;
  --muted:#7a7a7a;
  --panel:#f3f3f3;
  --white:#ffffff;
  --forest-dark:#1f3b38;
}
*{margin:0;padding:0;box-sizing:border-box}
html,body{width:1200px;height:3561px;overflow:hidden;background:var(--white)}
body{position:relative;font-family:"Open Sans",Arial,sans-serif;color:var(--ink)}
.abs{position:absolute}
.serif{font-family:"Libre Baskerville",Georgia,serif}
.btn{position:absolute;display:flex;align-items:center;justify-content:center;background:var(--blue);color:var(--white);font-size:16px;border-radius:3px;letter-spacing:.2px;box-shadow:0 2px 4px rgba(0,0,0,.12)}
.heading{position:absolute;left:0;width:1200px;text-align:center;font-family:"Libre Baskerville",Georgia,serif;font-weight:700;font-size:32px;letter-spacing:.5px}

/* header */
.site-header{position:absolute;left:0;top:0;width:1200px;height:115px;background:var(--white)}
.brand{position:absolute;left:118px;top:18px;width:120px;text-align:center}
.brand-dot{width:46px;height:46px;border-radius:50%;background:var(--teal);margin:0 auto 6px}
.brand-name{font-family:"Libre Baskerville",Georgia,serif;font-size:10px;letter-spacing:2px;color:#444;line-height:13px}
.brand-sub{font-size:6px;letter-spacing:1px;color:#777}
.nav{position:absolute;top:54px;left:528px;display:flex;gap:29px;font-family:"Libre Baskerville",Georgia,serif;font-size:11.5px;font-weight:700;letter-spacing:.4px}
.nav .active{color:var(--blue)}
.login{left:985px;top:37px;width:103px;height:43px;font-size:16px}

/* hero */
.hero{position:absolute;left:0;top:115px;width:1200px;height:558px;background:linear-gradient(180deg,#c9c7cf 0%,#8aa6a8 28%,#2e5a4c 55%,#3f6a4a 75%,#5d7b48 100%)}
.hero-title{top:330px;left:0;width:1200px;text-align:center;color:var(--white);font-family:"Libre Baskerville",Georgia,serif;font-weight:700;font-size:49px;letter-spacing:1px}
.hero-sub{top:392px;left:0;width:1200px;text-align:center;color:var(--white);font-size:20px;letter-spacing:.3px}
.hero-link{top:433px;left:0;width:1200px;text-align:center;color:#c9e03b;font-family:"Libre Baskerville",Georgia,serif;font-weight:700;font-size:11.5px;text-decoration:underline;letter-spacing:.3px}

.popup{position:absolute;left:923px;top:159px;width:259px;height:286px;background:var(--white);box-shadow:0 2px 8px rgba(0,0,0,.15);text-align:center}
.popup h3{margin-top:42px;font-family:"Libre Baskerville",Georgia,serif;font-size:15px;letter-spacing:.8px}
.popup p{margin:14px auto 0;width:220px;font-size:14px;line-height:21px;color:#444}
.popup .field{position:absolute;left:22px;top:133px;width:223px;height:50px;border:1px solid #aaa;text-align:left;padding-left:14px;line-height:48px;font-size:14px;color:#777}
.popup .subscribe{position:absolute;left:22px;top:193px;width:223px;height:48px;background:var(--teal);color:var(--white);font-family:"Libre Baskerville",Georgia,serif;font-weight:700;font-size:14px;letter-spacing:1px;line-height:48px}
.close{position:absolute;left:1151px;top:147px;width:38px;height:38px;border-radius:50%;background:var(--white);box-shadow:0 1px 4px rgba(0,0,0,.25);text-align:center;line-height:38px;font-size:19px;font-weight:600}

/* services */
.services{position:absolute;left:0;top:673px;width:1200px;height:815px;background:var(--panel)}
.photo{position:absolute}
.card-label{position:absolute;color:var(--white);font-family:"Libre Baskerville",Georgia,serif;font-weight:700;font-size:18px;letter-spacing:.5px}
.svc-text{position:absolute;width:470px;font-size:14.5px;line-height:29px;color:var(--muted);font-weight:300}

/* about */
.about-text{position:absolute;left:111px;top:1640px;width:477px;font-size:15px;line-height:35px;color:var(--muted);font-weight:300;text-align:justify}

/* mediation band */
.band{position:absolute;left:0;top:2027px;width:1200px;height:298px;background:linear-gradient(180deg,#6fc7b7 0%,#5fb5a8 55%,#4a9c8e 100%)}
.band-text{position:absolute;left:200px;top:2136px;width:800px;text-align:center;color:var(--white);font-size:15px;line-height:29px}
.quiz{left:445px;top:2209px;width:308px;height:51px;background:var(--lime);font-size:15px;border-radius:2px}

/* blog */
.post{position:absolute;top:2486px;height:408px;background:var(--white);box-shadow:0 1px 5px rgba(0,0,0,.15)}
.post .thumb{position:absolute;left:0;top:0;width:100%;height:214px}
.post .date{position:absolute;right:0;top:0;width:165px;height:40px;background:var(--teal);color:var(--white);font-size:16px;display:flex;align-items:center;justify-content:center;gap:12px}
.post h4{position:absolute;left:12px;top:234px;font-family:"Libre Baskerville",Georgia,serif;font-size:12.5px;letter-spacing:.6px}
.post p{position:absolute;left:12px;top:258px;width:285px;font-size:14.5px;line-height:25px;color:var(--muted);font-weight:300}
.post .btn{left:10px;top:344px;width:138px;height:48px}

/* newsletter */
.newsletter{position:absolute;left:0;top:3003px;width:1200px;height:318px;background:linear-gradient(180deg,#274a44 0%,#1f3b38 60%,#2b4a3c 100%)}
.nl-input{position:absolute;top:3177px;width:229px;height:62px;background:var(--white);font-size:15px;color:#777;padding-left:12px;line-height:62px}
.signup{position:absolute;left:859px;top:3177px;width:229px;height:62px;background:var(--teal);color:var(--white);font-family:"Libre Baskerville",Georgia,serif;font-weight:700;font-size:15px;letter-spacing:1px;text-align:center;line-height:62px}

/* footer */
.foot-text{position:absolute;font-size:15px;color:#777;line-height:34px}
.foot-links{position:absolute;font-size:15.5px;color:#777;line-height:26px}
.social{position:absolute;top:3372px;width:22px;height:22px;border-radius:50%;background:var(--ink)}
.copyright{position:absolute;left:0;top:3507px;width:1200px;text-align:center;font-size:15px;color:#777}
</style>
</head>
<body>

<header class="site-header">
  <div class="brand">
    <div class="brand-dot"></div>
    <div class="brand-name">BRIGHT HARBOR</div>
    <div class="brand-sub">LAW &amp; MEDIATION</div>
  </div>
  <nav class="nav">
    <span class="active">HOME</span><span>SERVICES</span><span>ABOUT</span><span>CONTACT</span><span>FAQ</span><span>BLOG</span>
  </nav>
  <div class="btn login">LOG IN</div>
</header>

<section class="hero" role="img" aria-label="Misty forested mountains above a calm lake with a dirt path"></section>
<div class="abs hero-title">BRIGHT HARBOR</div>
<div class="abs hero-sub">CHANGING THE WAY PEOPLE DIVORCE</div>
<div class="abs hero-link">SCHEDULE A FREE INFORMATION CALL</div>

<aside class="popup">
  <h3>KEEP IN TOUCH</h3>
  <p>Nemo enim ipsam voluptatem quia sit aspernatur aut</p>
  <div class="field">Email</div>
  <div class="subscribe">SUBSCRIBE</div>
</aside>
<div class="close">X</div>

<section class="services"></section>
<h2 class="heading" style="top:770px">OUR SERVICES</h2>
<div class="photo" style="left:111px;top:834px;width:479px;height:345px;background:linear-gradient(135deg,#5c4a44 0%,#cfc2b7 45%,#e8e3de 70%,#8aa0b8 100%)" role="img" aria-label="Couple meeting with a mediator on a sofa"></div>
<div class="card-label" style="left:236px;top:995px">DIVORCE MEDIATION</div>
<div class="photo" style="left:608px;top:834px;width:480px;height:345px;background:linear-gradient(135deg,#cfd6dc 0%,#9aa5ae 40%,#2e3338 70%,#d6d9dc 100%)" role="img" aria-label="Lawyer in a suit at a meeting table with clients"></div>
<div class="card-label" style="left:780px;top:1004px">DIVORCE LAWYER</div>
<p class="svc-text" style="left:111px;top:1201px">Mediation is possible when both spouses are willing to negotiate their divorce agreements in good faith, with the help of a neutral mediator. Bright Harbor™ attorney-mediators are experienced family</p>
<p class="svc-text" style="left:608px;top:1201px">If mediation is not possible, you need a lawyer to advise, negotiate, and possibly advocate for you. Our experienced Bright Harbor™ lawyers offer clear, confident, and highly effective advice and representation while attempting to minimize</p>
<div class="btn" style="left:111px;top:1331px;width:155px;height:52px">LEARN MORE</div>
<div class="btn" style="left:608px;top:1331px;width:155px;height:52px">LEARN MORE</div>

<h2 class="abs serif" style="left:111px;top:1583px;font-size:32px;font-weight:700;letter-spacing:.5px">ABOUT US</h2>
<p class="about-text">Long before meeting, attorneys Daniel Marsh and Owen Castell experienced firsthand the impact of divorce in their own lives. This personal experience only made it more important to them to work as hard as possible, as legal practitioners, to help people avoid the wreckage that contentious, litigious divorces leave behind. Upon meeting, the lawyers realized they held shared values</p>
<div class="btn" style="left:111px;top:1865px;width:155px;height:52px">READ MORE</div>
<div class="photo" style="left:629px;top:1590px;width:459px;height:336px;background:linear-gradient(135deg,#b9b4ad 0%,#6f6a66 35%,#d7d3cf 65%,#f1efec 100%)" role="img" aria-label="Family with two young children meeting an advisor at a table"></div>
<svg class="abs" style="left:820px;top:1720px" width="76" height="76" viewBox="0 0 76 76" aria-hidden="true">
  <circle cx="38" cy="38" r="36" fill="#33a6d7" stroke="#ffffff" stroke-width="3"/>
  <path d="M31 25 L53 38 L31 51 Z" fill="#ffffff"/>
</svg>

<section class="band" role="img" aria-label="Misty teal-toned pine forest"></section>
<h2 class="heading" style="top:2084px;color:#ffffff">MEDIATION OR LAWYER?</h2>
<p class="band-text">Our simple, free questionnaire can help you determine if you and your spouse are well suited for Bright Harbor™ mediation, or if you may want legal representation for yourself.</p>
<div class="btn quiz">TAKE OUR FREE QUESTIONNAIRE</div>

<h2 class="heading" style="top:2420px;left:-12px">LATEST BLOG</h2>

<article class="post" style="left:111px;width:313px">
  <div class="thumb" role="img" aria-label="Parents apart with an upset child between them" style="background:linear-gradient(135deg,#8c7e72 0%,#d9d2ca 50%,#c98a8a 75%,#5f6b78 100%)"></div>
  <div class="date"><svg width="16" height="16" viewBox="0 0 16 16"><rect x="1" y="2" width="14" height="13" fill="none" stroke="#fff" stroke-width="1.4"/><line x1="1" y1="6" x2="15" y2="6" stroke="#fff" stroke-width="1.4"/></svg>01-03-2020</div>
  <h4>LOREM IPSUM DOLOR SIT AMET</h4>
  <p>Nemo enim ipsam voluptatem quia sit aspernatur aut odit aut fugit, sed quia consequuntur</p>
  <div class="btn">READ MORE</div>
</article>
<article class="post" style="left:440px;width:316px">
  <div class="thumb" role="img" aria-label="Advisor in a suit meeting two clients in an office" style="background:linear-gradient(135deg,#d8dadc 0%,#7d8791 35%,#2b3540 60%,#e1e2e3 100%)"></div>
  <div class="date"><svg width="16" height="16" viewBox="0 0 16 16"><rect x="1" y="2" width="14" height="13" fill="none" stroke="#fff" stroke-width="1.4"/><line x1="1" y1="6" x2="15" y2="6" stroke="#fff" stroke-width="1.4"/></svg>20-02-2020</div>
  <h4>LOREM IPSUM DOLOR SIT AMET</h4>
  <p>Nemo enim ipsam voluptatem quia sit aspernatur aut odit aut fugit, sed quia consequuntur</p>
  <div class="btn">READ MORE</div>
</article>
<article class="post" style="left:771px;width:317px">
  <div class="thumb" role="img" aria-label="Smiling couple holding hands at a desk" style="background:linear-gradient(135deg,#c9ced4 0%,#5f7fa8 40%,#ece9e4 70%,#b08a68 100%)"></div>
  <div class="date"><svg width="16" height="16" viewBox="0 0 16 16"><rect x="1" y="2" width="14" height="13" fill="none" stroke="#fff" stroke-width="1.4"/><line x1="1" y1="6" x2="15" y2="6" stroke="#fff" stroke-width="1.4"/></svg>18-01-2020</div>
  <h4>LOREM IPSUM DOLOR SIT AMET</h4>
  <p>Nemo enim ipsam voluptatem quia sit aspernatur aut odit aut fugit, sed quia consequuntur</p>
  <div class="btn">READ MORE</div>
</article>

<section class="newsletter" role="img" aria-label="Dark misty forest and lake"></section>
<h2 class="heading" style="top:3075px;color:#ffffff">SUBSCRIBE TO OUR NEWSLETTER</h2>
<p class="abs" style="left:0;top:3126px;width:1200px;text-align:center;color:#ffffff;font-size:16px">Sign up to receive news and updates.</p>
<div class="nl-input" style="left:112px">First Name</div>
<div class="nl-input" style="left:361px">Last Name</div>
<div class="nl-input" style="left:610px">Email Address</div>
<div class="signup">SIGN UP</div>

<footer>
  <div class="brand" style="left:112px;top:3368px">
    <div class="brand-dot" style="width:58px;height:58px"></div>
    <div class="brand-name" style="font-size:11px">BRIGHT HARBOR</div>
    <div class="brand-sub">LAW &amp; MEDIATION</div>
  </div>
  <div class="foot-text" style="left:347px;top:3363px">Bright Harbor Family Law &amp; Mediation LLC<br>1420 Alder Street, Suite 2<br>Cedar Ridge, Colorado 80999</div>
  <div class="foot-links" style="left:738px;top:3367px">Home<br>Services<br>About<br>Contact</div>
  <div class="foot-links" style="left:842px;top:3367px">FAQ<br>Blog<br>Resources<br>Testimonials</div>
  <div class="social" style="left:1035px" aria-label="Social profile"></div>
  <div class="social" style="left:1072px" aria-label="Social profile"></div>
  <div class="copyright">© 2020 All Rights Reserved</div>
</footer>

</body>
</html>
```